Website for luxury cleaning company

Established in 2014, the business offers office cleaning, floor treatment, carpet cleaning, and window cleaning for businesses with office space in the Greater Toronto area. The business was founded by Felix Handorf

Verity's premium shine Inc. Needs a new wordpress website
(VPS) seeks to ensure that businesses have a spotless office environment to support the work they do. Our focus is on Commercial cleaning the website should be a catalyst in connecting business professionals with our environmental cleaning solutions. Focusing on small offices will establish the reputation of the company by working with a variety of clients and will force the streamlining of operations.

The design needs to be elegant and attractive to potential corporate clients and reflect the high level of sophistication of the luxury cleaning service demographic. It needs to be very graphic with high-impact photos and the ability to inspire action. Although it can be simple now it will need to have the capability of expanding to allow acceptance of payments online, offering of information products in exchange for email registration, and potentially a membership-oriented section of the site with forums and special savings

At the present time, it is more of an information-oriented site that tells a compelling story and inspires people to take action to get involved in the way that most fits their cleaning needs.

We need to have the ability to add pages and blog posts easily on our own while maintaining a relationship that would allow us a cost-effective way of making more major additions and adjustments to the site.
(Match the text logo with the correct VPS logo colour)
Attached is our logo we have included a few colour variations, we will continue to work with the wining designer on future projects for our 2014 fiscal year, thanks for your dedication to our project
SOCIAL MEDIA LINKS SHOULD BE PRESENT THE OPTION TO ADD/VIDEO AND PODCAST SHOULD BE THERE AS WELL

CONVERT EPS FILES TO JPEG OR GIF FOR BETTER QUALITY WHEN VIEWED ON WEB

Designers please submit 3 or minimum 2 designs
Updates

Hope you all had a great weekend the marketing team looks forward to seeing your designs. Remember keep it clean sometimes lees is more, we are open to all concepts at this stage so feel free to contact us about anything. Thanks again from VPS INC. 

Hi guys there is one day left in the competition please submit any final revisions by tomorrow we look forward to seeing your creative designs.

Target Market(s)

The market currently consists of 40,000 small, medium, and large office businesses. Healthy growth is expected for this market, especially for small offices which will be the initial target market for the business. Focusing on small offices will establish the reputation of the company by working with a variety of clients and will force the streamlining of operations.

Industry/Entity Type

Cleaning Service

Requirements
Must have
• Corporate looking we are open minded and want designers to use their creativity.
A way for clients to pre pay for services. mailing list, employment form
Nice to have
• podcast option, video player, social media links
Should not have
• NO generic or stock footage.

```html
<!DOCTYPE html>
<html lang="en">
<head>
<meta charset="utf-8">
<title>Verity's Premium Shine Inc.</title>
<link rel="stylesheet" href="https://fonts.googleapis.com/css2?family=Tinos:wght@400;700&family=Open+Sans:wght@400&family=Jost:ital,wght@1,500&display=swap">
<style>
:root{
  --gold:#c0912a;
  --gold-light:#d9aa45;
  --gold-dark:#9a6f17;
  --ink:#3a3a3a;
  --text:#4a4a4a;
  --page:#ececec;
  --card:#f4f4f4;
  --line:#cfcfcf;
  --nav:rgba(40,36,34,.82);
  --footer:#141414;
  --white:#ffffff;
}
*{box-sizing:border-box;margin:0;padding:0}
html,body{width:672px;height:1200px;overflow:hidden}
body{position:relative;background:linear-gradient(#f3f3f3,#e6e6e6);font-family:"Open Sans",sans-serif;color:var(--text)}
.abs{position:absolute}

/* hero */
.hero{left:0;top:0;width:672px;height:380px;border-bottom:3px solid var(--gold);
  background:
    linear-gradient(180deg,rgba(0,0,0,0) 0%,rgba(0,0,0,0) 66%,rgba(196,128,62,.9) 80%,rgba(206,138,70,1) 100%),
    linear-gradient(90deg,#c7ccd0 0%,#b9bec2 22%,#e9e4dc 30%,#5a3e2e 42%,#4a3325 62%,#efe2cf 78%,#caa27f 100%)}
.brand{left:54px;top:20px;width:196px;height:70px;background:linear-gradient(#f7f7f7,#cfcfcf);clip-path:polygon(0 0,100% 0,82% 100%,0 100%);display:flex;align-items:center;padding-left:14px}
.brand-name{font-family:"Tinos",serif;font-size:15px;color:var(--gold);line-height:1.1;width:130px}
.main-nav{left:250px;top:22px;width:368px;height:67px;background:var(--nav)}
.nav-item{position:absolute;top:0;width:90px;margin-left:-45px;text-align:center;color:var(--white);font-family:"Tinos",serif;font-size:8px;letter-spacing:.5px}
.nav-item svg{display:block;margin:19px auto 8px}
.slogan{right:58px;font-family:"Jost",sans-serif;font-style:italic;font-weight:500;color:var(--white);font-size:14px;letter-spacing:1px;background:var(--gold);box-shadow:0 3px 0 #2a2119;display:flex;align-items:center;justify-content:center;height:28px}
.slogan-1{top:163px;width:258px}
.slogan-2{top:197px;width:201px}

/* welcome */
.welcome-title{left:0;top:405px;width:672px;text-align:center;font-family:"Tinos",serif;font-weight:400;font-size:13px;color:var(--ink);letter-spacing:.3px}
.welcome-title em{font-style:normal;color:var(--gold)}
.rule-double{top:435px;height:4px;border-top:1px solid var(--line);border-bottom:1px solid var(--line)}
.video{left:54px;top:457px;width:214px;height:131px;background:linear-gradient(#8ea0ae,#44525d 60%,#1b1f24)}
.video-bar{left:54px;top:578px;width:214px;height:10px;background:#111}
.video-progress{left:54px;top:577px;width:35px;height:2px;background:#d0201b}
.play{left:146px;top:508px;width:30px;height:20px;background:rgba(20,20,20,.85);border-radius:4px}
.intro{left:306px;top:456px;width:292px;font-size:8px;line-height:12px;color:var(--text)}
.intro p+p{margin-top:12px}
.rule{left:54px;width:564px;height:1px;background:var(--line)}

/* features */
.feature{top:648px;width:178px;height:206px;background:var(--card);border:1px solid #d8d8d8;border-bottom:2px solid var(--gold);text-align:center}
.feature-img{margin:9px 0 0 7px;width:162px;height:83px;border:2px solid #ddd}
.feature h3{font-family:"Tinos",serif;font-weight:400;font-size:10.5px;color:var(--ink);margin-top:8px;letter-spacing:.4px}
.feature p{font-size:8px;line-height:12px;margin:3px 12px 0}
.btn-more{display:inline-block;margin-top:10px;width:69px;height:14px;border-radius:7px;background:linear-gradient(var(--gold-light),var(--gold-dark));color:var(--white);font-family:"Tinos",serif;font-size:7px;line-height:14px;letter-spacing:.4px}

/* blog */
.blog-title{left:74px;top:906px;font-family:"Tinos",serif;font-weight:400;font-size:12.5px;color:var(--ink);letter-spacing:.4px}
.blog-title em{font-style:normal;color:var(--gold)}
.article{left:73px;width:358px;height:89px;background:#f1f1f1;border:1px solid #dcdcdc;border-radius:3px}
.article-img{left:6px;top:13px;width:109px;height:64px;border:2px solid #ddd;background:linear-gradient(135deg,#6b6b6b,#b79b6e 60%,#8c7348)}
.article h4{position:absolute;left:124px;top:11px;font-family:"Tinos",serif;font-weight:400;font-size:10.5px;color:var(--ink);letter-spacing:.3px}
.article hr{position:absolute;left:124px;top:27px;width:220px;border:0;border-top:1px solid var(--line)}
.article p{position:absolute;left:124px;top:34px;width:225px;font-size:7.6px;line-height:11px}

.quote{left:456px;top:930px;width:153px;height:184px;background:#ebebeb;border:1px solid #c9c9c9;border-radius:3px;overflow:hidden}
.quote-head{height:21px;background:linear-gradient(#3a3a3a,#111);color:var(--white);font-family:"Tinos",serif;font-size:7.5px;letter-spacing:.7px;text-align:center;line-height:21px}
.field{position:absolute;left:6px;width:138px;background:var(--white);border:1px solid #bdbdbd;border-radius:3px;font-size:7.5px;color:#aaa;padding:3px 7px}
.btn-send{position:absolute;left:8px;top:152px;width:135px;height:18px;background:linear-gradient(var(--gold-light),var(--gold-dark));color:var(--white);font-family:"Tinos",serif;font-size:7.5px;letter-spacing:.6px;text-align:center;line-height:18px;border-radius:2px}

/* footer */
.site-footer{left:0;top:1144px;width:672px;height:56px;background:linear-gradient(#2a2a2a,var(--footer));border-bottom:3px solid var(--gold)}
.footer-links{left:82px;top:18px;font-family:"Tinos",serif;font-size:7.5px;color:#d8d8d8;letter-spacing:.4px}
.footer-legal{left:236px;top:13px;width:200px;text-align:center;font-family:"Tinos",serif;font-size:7.5px;line-height:10px;color:#d8d8d8;letter-spacing:.3px}
.social{top:15px;width:14px;height:14px;border-radius:50%;background:#d4d4d4}
</style>
</head>
<body>

<header class="abs hero" role="img" aria-label="Photo of a bright modern office interior with window wall, dark wood panelling, desks, meeting table, chairs and a frosted glass screen"></header>
<div class="abs brand"><span class="brand-name">Verity's premium shine Inc.</span></div>
<nav class="abs main-nav">
  <div class="nav-item" style="left:20px">
    <svg width="18" height="16" viewBox="0 0 18 16"><path d="M9 1 1 8h2v7h4v-5h4v5h4V8h2z" fill="#fff"/></svg>HOME</div>
  <div class="nav-item" style="left:100px">
    <svg width="16" height="16" viewBox="0 0 16 16"><circle cx="8" cy="5" r="4" fill="#fff"/><path d="M1 16c0-5 3-6 7-6s7 1 7 6z" fill="#fff"/></svg>ABOUT US</div>
  <div class="nav-item" style="left:199px">
    <svg width="18" height="16" viewBox="0 0 18 16" fill="none" stroke="#fff" stroke-width="1.6"><path d="M9 1 1 5l8 4 8-4z" fill="#fff"/><path d="M1 8l8 4 8-4M1 11l8 4 8-4"/></svg>OUR SERVICES</div>
  <div class="nav-item" style="left:304px">
    <svg width="20" height="16" viewBox="0 0 20 16" fill="none" stroke="#fff" stroke-width="1.3"><rect x="1" y="2" width="18" height="12"/><path d="M1 2l9 7 9-7"/></svg>CONTACT US</div>
</nav>
<div class="abs slogan slogan-1">YOUR HEADING TEXT OR SLOGAN</div>
<div class="abs slogan slogan-2">SECOND LINE GOES HERE</div>

<h1 class="abs welcome-title">Welcome to <em>Verity's Premium Shine</em></h1>
<div class="abs rule-double" style="left:54px;width:268px"></div>
<div class="abs rule-double" style="left:350px;width:268px"></div>

<div class="abs video" role="img" aria-label="Video still of a cleaner with a cart in a bright glass hall"></div>
<div class="abs video-bar"></div>
<div class="abs video-progress"></div>
<div class="abs play"></div>
<svg class="abs" style="left:157px;top:513px" width="9" height="10" viewBox="0 0 9 10"><path d="M0 0l9 5-9 5z" fill="#fff"/></svg>

<div class="abs intro">
  <p>Lorem ipsum dolor sit amet, consectetur adipiscing elit. Donec laoreet tempus sapien et viverra. Suspendisse euismod viverra scelerisque. Duis mauris quam, feugiat luctus sagittis nec, mattis non lorem. Cras tempus ut ligula cursus placerat. Praesent commodo ac lorem sit amet tempor. Suspendisse euismod viverra scelerisque.</p>
  <p>Duis mauris quam, feugiat luctus sagittis nec, mattis non lorem. Cras tempus ut ligula cursus placerat. Praesent commodo ac lorem sit amet tempor. Suspendisse euismod viverra scelerisque feugiat luctus sagittis nec, mattis non lorem ut ligula cursus placerat.</p>
</div>
<div class="abs rule" style="top:613px"></div>

<section class="abs feature" style="left:55px">
  <div class="feature-img" role="img" aria-label="Team photo of the cleaning staff in uniforms" style="background:linear-gradient(#3e5a6e,#5b7486 50%,#2f3b45)"></div>
  <h3>Who we are</h3>
  <p>Lorem ipsum dolor consectetur adipiscing elit. Nulla auctor cursus commodo. Donec elementum tellus a dapibus rhoncus.</p>
  <span class="btn-more">Read more</span>
</section>
<section class="abs feature" style="left:247px">
  <div class="feature-img" role="img" aria-label="Window cleaners working on large office windows" style="background:linear-gradient(#8fb7de,#a9c7e0 55%,#4f7a3a 75%,#1b1f1c)"></div>
  <h3>What we offer</h3>
  <p>Lorem ipsum dolor consectetur adipiscing elit. Nulla auctor cursus commodo. Donec elementum tellus a dapibus rhoncus.</p>
  <span class="btn-more">Read more</span>
</section>
<section class="abs feature" style="left:439px">
  <div class="feature-img" role="img" aria-label="White jigsaw puzzle with a piece being placed" style="background:linear-gradient(135deg,#f5f5f5,#d9d9d9 70%,#c9a58c)"></div>
  <h3>Join our team</h3>
  <p>Lorem ipsum dolor consectetur adipiscing elit. Nulla auctor cursus commodo. Donec elementum tellus a dapibus rhoncus.</p>
  <span class="btn-more">Read more</span>
</section>

<div class="abs rule" style="top:897px"></div>
<h2 class="abs blog-title">Blog <em>Articles</em></h2>

<article class="abs article" style="top:930px">
  <div class="abs article-img" role="img" aria-label="Office chair bases on a patterned floor"></div>
  <h4>Article title goes here lorem ipsum sample</h4>
  <hr>
  <p>Lorem ipsum ut ligula cursus placerat commodo ac lorem sit amet tempor. Suspendisse euismod viverra scelerisque feugiat luctus sit amet tempor cursus placerat commodo cursus placerat tempus.</p>
</article>
<article class="abs article" style="top:1026px">
  <div class="abs article-img" role="img" aria-label="Office chair bases on a patterned floor"></div>
  <h4>Article title goes here lorem ipsum sample</h4>
  <hr>
  <p>Lorem ipsum ut ligula cursus placerat commodo ac lorem sit amet tempor. Suspendisse euismod viverra scelerisque feugiat luctus sit amet tempor cursus placerat commodo cursus placerat tempus.</p>
</article>

<aside class="abs quote">
  <div class="quote-head">GET A FREE QUOTE</div>
  <div class="field" style="top:30px;height:19px">Firstname</div>
  <div class="field" style="top:56px;height:19px">Email Address</div>
  <div class="field" style="top:82px;height:60px">Message</div>
  <div class="btn-send">SEND MESSAGE</div>
</aside>

<footer class="abs site-footer">
  <div class="abs footer-links">Privacy Policy &nbsp;-&nbsp; Terms &amp; Agreement</div>
  <div class="abs footer-legal">Verity's premium shine Inc.<br>Copyright © 2014</div>
  <div class="abs social" style="left:539px"></div>
  <div class="abs social" style="left:561px"></div>
  <div class="abs social" style="left:583px"></div>
</footer>

</body>
</html>
```